Industrial Professional Business Card Design (Vantrel KX)

Would like professional looking business cards. Not too busy leaning towards minimal. Should have a slogan like:
"Industrial Automation and Control".

We are a tech company that programs industrial PLC computers. We also develop custom hardware solutions. Please use the logo for inspiration.

Target Market(s)

Mining, industrial, processing, automation, factory

Industry/Entity Type

Engineering

Contact Information for Business Card

Name, phone, email, website. job title.

Font styles to use
Other font styles liked:
• droid sans

Requirements
Must have
• Use colours that go well with the logo. Not too busy design.

```html
<!DOCTYPE html>
<html lang="en">
<head>
<meta charset="utf-8">
<title>Vantrel KX — Business Card</title>
<link href="https://fonts.googleapis.com/css2?family=Open+Sans:wght@400;600;700&display=swap" rel="stylesheet">
<style>
  :root {
    --bg: #e6e6e4;
    --paper: #ffffff;
    --navy: #1c2a57;
    --navy-deep: #1a2150;
    --teal: #22709a;
    --orange: #f26a1b;
    --rule: #7a8199;
    --ink: #2a3358;
  }
  * { box-sizing: border-box; margin: 0; padding: 0; }
  html, body {
    width: 1200px; height: 801px; overflow: hidden;
    background: var(--bg);
    font-family: "Open Sans", sans-serif;
  }
  .stage {
    position: relative; width: 1200px; height: 801px;
    display: flex; align-items: center; justify-content: center; gap: 60px;
  }
  .card {
    position: relative; width: 520px; height: 297px;
    border-bottom: 4px solid var(--orange);
    box-shadow: 0 6px 18px rgba(0,0,0,0.12);
  }
  /* Front */
  .card-front { background: var(--paper); display: flex; align-items: center; }
  .front-brand {
    flex: 0 0 50%; display: flex; align-items: center; justify-content: center; gap: 10px;
  }
  .brand-dot { width: 22px; height: 22px; border-radius: 50%; background: var(--orange); }
  .brand-name { font-weight: 600; font-size: 34px; color: var(--navy); letter-spacing: 0.5px; }
  .divider { width: 1px; height: 120px; background: var(--rule); }
  .front-details { padding-left: 28px; color: var(--ink); }
  .person-name { color: var(--orange); font-weight: 700; font-size: 20px; line-height: 1.1; }
  .person-role { font-size: 14px; margin-bottom: 12px; }
  .address { font-size: 13px; line-height: 1.3; margin-bottom: 10px; }
  .contact-list { list-style: none; font-size: 13px; line-height: 1.6; }
  .contact-list li { display: flex; align-items: center; gap: 8px; }
  .contact-list svg { width: 12px; height: 12px; flex: none; }
  .web-accent { color: var(--orange); }
  /* Back */
  .card-back {
    background: linear-gradient(160deg, var(--navy-deep) 0%, var(--teal) 85%);
    display: flex; align-items: center; justify-content: center; gap: 14px;
  }
  .card-back .brand-dot { background: #ffffff; width: 26px; height: 26px; }
  .card-back .brand-name { color: #ffffff; font-size: 44px; }
</style>
</head>
<body>
<main class="stage">
  <section class="card card-front" aria-label="Business card front">
    <div class="front-brand">
      <span class="brand-dot"></span>
      <span class="brand-name">Vantrel KX</span>
    </div>
    <div class="divider"></div>
    <div class="front-details">
      <p class="person-name">Dorian Kessel</p>
      <p class="person-role">Manager</p>
      <p class="address">Your address, city<br>state, ZIP 0000</p>
      <ul class="contact-list">
        <li>
          <svg viewBox="0 0 12 12" aria-hidden="true"><path d="M2.5 1h2l1 2.6-1.3 1a6 6 0 0 0 2.7 2.7l1-1.3L11 7v2c0 .6-.4 1-1 1A9 9 0 0 1 1.5 2c0-.6.4-1 1-1z" fill="var(--orange)"/></svg>
          123-456-2100
        </li>
        <li>
          <svg viewBox="0 0 12 12" aria-hidden="true"><rect x="1" y="2.5" width="10" height="7" rx="1" fill="none" stroke="var(--orange)" stroke-width="1.3"/><path d="M1.5 3l4.5 3.5L10.5 3" fill="none" stroke="var(--orange)" stroke-width="1.3"/></svg>
          youremail@mailbox.com
        </li>
        <li>
          <svg viewBox="0 0 12 12" aria-hidden="true"><circle cx="6" cy="6" r="5" fill="var(--orange)"/><path d="M1 6h10M6 1c-2 2.5-2 7.5 0 10M6 1c2 2.5 2 7.5 0 10" fill="none" stroke="#fff" stroke-width="0.8"/></svg>
          <span>www.<span class="web-accent">yourwebsite</span>.com</span>
        </li>
      </ul>
    </div>
  </section>

  <section class="card card-back" aria-label="Business card back">
    <span class="brand-dot"></span>
    <span class="brand-name">Vantrel KX</span>
  </section>
</main>
</body>
</html>
```